Cardiology practice business card

We need a business card for our cardiology practice "Wattle Cardiology". We have a new logo, attached below. We like the colours in the logo - red and charcoal. The front of the business card will need to have the doctors name, address, phone number and email. The back will need to have space to write 2 appointment dates and times.

```html
<!DOCTYPE html>
<html lang="en">
<head>
<meta charset="utf-8">
<title>Wattle Cardiology – Business Card</title>
<link rel="stylesheet" href="https://fonts.googleapis.com/css2?family=Montserrat:wght@700&family=Roboto:wght@400;500;700&display=swap">
<style>
  :root {
    --red: #e3141b;
    --charcoal: #2e2e2f;
    --charcoal-deep: #232324;
    --ink: #3a3a3a;
    --label: #555555;
    --rule: #9a9a9a;
    --dash: #b8b8b8;
    --paper: #ffffff;
    --stage: #e9e9eb;
  }
  * { box-sizing: border-box; margin: 0; padding: 0; }
  html, body { width: 1200px; height: 840px; overflow: hidden; }
  body {
    background: var(--stage);
    font-family: "Roboto", Arial, sans-serif;
    color: var(--ink);
    position: relative;
  }
  .card {
    position: absolute;
    top: 260px;
    width: 560px;
    height: 320px;
    border-radius: 24px;
    background: var(--paper);
    border-bottom: 5px solid var(--red);
    border-right: 2px solid var(--red);
    overflow: hidden;
    box-shadow: 0 10px 26px rgba(0,0,0,.18);
  }
  .card--back { left: 26px; }
  .card--front { left: 614px; }

  /* Shared wordmark */
  .wordmark {
    font-family: "Montserrat", Arial, sans-serif;
    font-weight: 700;
    font-size: 26px;
    letter-spacing: 1px;
    text-transform: uppercase;
    white-space: nowrap;
    color: var(--red);
    display: flex; align-items: center; gap: 10px;
  }
  .wordmark__dot { width: 14px; height: 14px; border-radius: 50%; background: var(--red); flex: none; }

  /* Back: appointment card */
  .back__band {
    position: absolute; left: 0; top: 0; width: 100%; height: 138px;
    background: linear-gradient(160deg, var(--charcoal), var(--charcoal-deep));
  }
  .back__wordmark { position: absolute; left: 34px; top: 50px; }
  .appointments {
    position: absolute; left: 60px; right: 40px; top: 160px;
    display: flex; flex-direction: column; gap: 22px;
  }
  .slot { display: flex; flex-direction: column; gap: 22px; }
  .slot__note { border-top: 1.5px dashed var(--dash); height: 0; }
  .slot__row { display: flex; align-items: flex-end; gap: 10px; font-size: 14px; letter-spacing: 1px; color: var(--label); line-height: 16px; }
  .slot__line { flex: 1; border-bottom: 1.2px solid #444; margin-bottom: 3px; }

  /* Front: contact card */
  .front__wordmark { position: absolute; right: 40px; top: 46px; }
  .front__rule { position: absolute; left: 210px; right: 30px; top: 150px; border-top: 1.5px solid var(--rule); }
  .person { position: absolute; left: 44px; top: 168px; }
  .person__name { font-size: 22px; font-weight: 700; color: var(--red); text-transform: uppercase; letter-spacing: .2px; }
  .person__role { font-size: 16px; color: var(--ink); margin-top: 2px; }
  .person__rule { width: 190px; border-top: 1.2px solid #555; margin-top: 8px; }
  .contact { position: absolute; left: 44px; top: 238px; list-style: none; font-size: 15px; line-height: 22px; }
  .contact li { display: flex; align-items: center; gap: 8px; }
  .contact svg { width: 14px; height: 14px; fill: var(--red); flex: none; }
  .address { position: absolute; right: 34px; top: 176px; text-align: right; font-size: 15px; line-height: 20px; color: var(--label); }
</style>
</head>
<body>
  <section class="card card--back" aria-label="Appointment card, back">
    <div class="back__band">
      <div class="wordmark back__wordmark"><span class="wordmark__dot"></span>Wattle Cardiology</div>
    </div>
    <div class="appointments">
      <div class="slot">
        <div class="slot__note"></div>
        <div class="slot__row">
          <span>DATE</span><span class="slot__line"></span>
          <span>TIME</span><span class="slot__line"></span>
        </div>
      </div>
      <div class="slot">
        <div class="slot__note"></div>
        <div class="slot__row">
          <span>DATE</span><span class="slot__line"></span>
          <span>TIME</span><span class="slot__line"></span>
        </div>
      </div>
    </div>
  </section>

  <section class="card card--front" aria-label="Business card, front">
    <div class="wordmark front__wordmark"><span class="wordmark__dot"></span>Wattle Cardiology</div>
    <div class="front__rule"></div>
    <div class="person">
      <p class="person__name">Jonathan Smith</p>
      <p class="person__role">Manager</p>
      <div class="person__rule"></div>
    </div>
    <ul class="contact">
      <li><svg viewBox="0 0 16 16"><path d="M3 1h3l1 4-2 1a9 9 0 0 0 5 5l1-2 4 1v3a2 2 0 0 1-2 2A13 13 0 0 1 1 3a2 2 0 0 1 2-2z"/></svg>123-456-2100</li>
      <li><svg viewBox="0 0 16 16"><path d="M1 3h14v10H1z M1 3l7 6 7-6" stroke="#fff" stroke-width="1"/></svg>youremail@mailhub.com</li>
      <li><svg viewBox="0 0 16 16"><circle cx="8" cy="8" r="7"/><path d="M1 8h14M8 1c3 3 3 11 0 14M8 1c-3 3-3 11 0 14" stroke="#fff" stroke-width="1" fill="none"/></svg>www.yourwebsite.com</li>
    </ul>
    <p class="address">Your Address, City<br>State, Zip 0000</p>
  </section>
</body>
</html>
```